Weight Loss Banner Ad

We need banner ads for our website, www.brightplatekitchen.com. We would like to see Banner ads that represent what you think is the most captivating aspect of The MealWise Plan. Please review the website.

The banner ad should be something you REALLY want to click on. It needs to include the name and/or logo and the slogan "Gourmet Meals Direct To Your House"

We will want the final ad in multiple sizes but it should use the same image and copy.

Logo is attached, so are images. Feel free to use your own if you think you have a better on

Size (pixels):
468 x 60
392 x 72
234 x 60
125 x 125
120 x 90
120 x 60
88 x 31
120 x 240
120 x 600
160 x 600

Target Market(s)

Fitness Enthusiast looking to lose weight.

Industry/Entity Type

Weight

Font styles to use
Sans Serif

Requirements
Must have
• See Description
Nice to have
• Should be awesome and make you want to buy some food. Also you may want to say something about the price:

i.e. Starting at only $99

```html
<!DOCTYPE html>
<html lang="en">
<head>
<meta charset="utf-8">
<title>The MealWise Plan — Banner Set</title>
<link href="https://fonts.googleapis.com/css2?family=PT+Sans:wght@400;700&display=swap" rel="stylesheet">
<style>
  :root{
    --page:#ffffff;
    --ink:#1d1d1d;
    --panel:#2a2a2a;
    --band:#4d4d4d;
    --band-dark:#333333;
    --lime:#8dc63f;
    --button:#6dbd2a;
    --button-edge:#2e5a0f;
    --url-bar:#141414;
    --white:#ffffff;
  }
  *{box-sizing:border-box;margin:0;padding:0}
  html,body{width:667px;height:1200px;overflow:hidden;background:var(--page)}
  body{position:relative;font-family:"PT Sans",sans-serif;color:var(--ink)}

  .banner{position:absolute;background:var(--panel);overflow:hidden}
  .banner .logo-area{position:absolute;left:0;top:0;background:var(--white);display:flex;align-items:center;justify-content:center;text-align:center}
  .brand-name{color:var(--lime);font-weight:700;line-height:1}
  .headline{position:absolute;left:0;right:0;color:var(--white);font-weight:700;text-align:center;text-transform:uppercase}
  .tagline{position:absolute;left:0;right:0;color:var(--lime);text-align:center;font-weight:400}
  .price-band{position:absolute;left:0;right:0;background:var(--band);display:flex;align-items:stretch}
  .price-band .starting{flex:1;color:var(--lime);text-transform:uppercase;display:flex;align-items:center;justify-content:center;text-align:center;font-weight:400}
  .price-band .price{background:var(--band-dark);color:var(--white);font-weight:700;display:flex;align-items:center;justify-content:center}
  .join-button{position:absolute;background:var(--button);border:2px solid var(--button-edge);border-radius:6px;color:var(--ink);font-weight:400;display:flex;align-items:center;justify-content:center;text-transform:uppercase}
  .food-photo{position:absolute;background:linear-gradient(160deg,#8fb55a 0%,#c8c8bd 28%,#9a5a35 52%,#5a3a25 72%,#d9c49b 100%)}
  .swoosh{position:absolute;display:block}
  .url-bar{position:absolute;left:0;right:0;bottom:0;background:var(--url-bar);color:var(--white);display:flex;align-items:center;justify-content:center}

  .size-label{position:absolute;font-weight:700;font-size:24px;color:var(--ink);text-align:center}

  /* 160x600 skyscraper */
  .skyscraper{left:15px;top:28px;width:294px;height:1107px}
  .skyscraper .logo-area{width:294px;height:153px}
  .skyscraper .brand-name{font-size:42px}
  .skyscraper .headline{top:190px;font-size:52px;line-height:56px}
  .skyscraper .tagline{top:378px;font-size:27px;line-height:32px}
  .skyscraper .price-band{top:470px;height:90px}
  .skyscraper .starting{font-size:24px;line-height:27px}
  .skyscraper .price{width:136px;font-size:68px}
  .skyscraper .join-button{left:30px;top:580px;width:235px;height:54px;font-size:27px}
  .skyscraper .food-photo{left:0;top:640px;width:294px;height:425px}
  .skyscraper .swoosh{left:0;top:610px}
  .skyscraper .url-bar{height:42px;font-size:25px}

  /* 120x240 vertical */
  .vertical{left:377px;top:28px;width:221px;height:441px}
  .vertical .logo-area{width:221px;height:70px}
  .vertical .brand-name{font-size:28px}
  .vertical .headline{top:80px;font-size:27px;line-height:30px}
  .vertical .tagline{top:146px;font-size:19px;line-height:22px}
  .vertical .price-band{top:200px;height:58px}
  .vertical .starting{font-size:15px;line-height:17px}
  .vertical .price{width:100px;font-size:44px}
  .vertical .food-photo{left:0;top:268px;width:221px;height:173px}
  .vertical .swoosh{left:0;top:256px}
  .vertical .join-button{left:112px;top:399px;width:102px;height:32px;font-size:15px}

  /* 125x125 square */
  .square{left:328px;top:539px;width:326px;height:274px}
  .square .logo-area{width:175px;height:64px}
  .square .brand-name{font-size:22px}
  .square .headline{width:175px;top:72px;font-size:24px;line-height:25px}
  .square .tagline{width:175px;top:125px;font-size:16px;line-height:18px}
  .square .price-band{width:175px;top:168px;height:46px}
  .square .starting{font-size:12px;line-height:14px}
  .square .price{width:80px;font-size:36px}
  .square .join-button{left:12px;top:222px;width:112px;height:26px;font-size:13px}
  .square .food-photo{left:175px;top:0;width:151px;height:274px}
  .square .swoosh{left:150px;top:0}
  .square .url-text{position:absolute;left:0;width:175px;top:252px;color:var(--white);font-size:13px;text-align:center}
</style>
</head>
<body>

  <section class="banner skyscraper" aria-label="160 by 600 banner">
    <div class="logo-area"><span class="brand-name">The MealWise<br>Plan</span></div>
    <h1 class="headline">Effortless<br>Weight<br>Loss</h1>
    <p class="tagline">Gourmet Meals<br>Direct To Your House</p>
    <div class="price-band">
      <span class="starting">Starting<br>at only</span>
      <span class="price">$99</span>
    </div>
    <div class="join-button">Join now &gt;&gt;</div>
    <div class="food-photo" role="img" aria-label="Photo of gourmet plated meals: grilled steak strips, lettuce wraps, roasted vegetables and dip"></div>
    <svg class="swoosh" width="294" height="60" viewBox="0 0 294 60" aria-hidden="true">
      <path d="M0 60 Q150 40 294 0 L294 20 Q150 55 0 60 Z" fill="var(--lime)"/>
    </svg>
    <div class="url-bar">brightplatekitchen.com</div>
  </section>
  <div class="size-label" style="left:15px;top:1146px;width:294px">160x600</div>

  <section class="banner vertical" aria-label="120 by 240 banner">
    <div class="logo-area"><span class="brand-name">The MealWise Plan</span></div>
    <h2 class="headline">Effortleass<br>Weight Loss</h2>
    <p class="tagline">Gourmet Meals<br>Direct To Your House</p>
    <div class="price-band">
      <span class="starting">Starting<br>at only</span>
      <span class="price">$99</span>
    </div>
    <div class="food-photo" role="img" aria-label="Photo of gourmet plated meals with steak and roasted vegetables"></div>
    <svg class="swoosh" width="221" height="40" viewBox="0 0 221 40" aria-hidden="true">
      <path d="M0 30 Q110 22 221 0 L221 14 Q110 38 0 40 Z" fill="var(--lime)"/>
    </svg>
    <div class="join-button">Join now &gt;&gt;</div>
  </section>
  <div class="size-label" style="left:377px;top:480px;width:221px">120x240</div>

  <section class="banner square" aria-label="125 by 125 banner">
    <div class="food-photo" role="img" aria-label="Photo of gourmet plated meals with roasted vegetables and dip"></div>
    <svg class="swoosh" width="60" height="274" viewBox="0 0 60 274" aria-hidden="true">
      <path d="M25 0 Q50 140 28 274 L38 274 Q60 140 40 0 Z" fill="var(--lime)"/>
    </svg>
    <div class="logo-area"><span class="brand-name">The MealWise<br>Plan</span></div>
    <h2 class="headline">Effortless<br>Weight Loss</h2>
    <p class="tagline">Gourmet Meals<br>Direct To Your House</p>
    <div class="price-band">
      <span class="starting">Starting<br>at only</span>
      <span class="price">$99</span>
    </div>
    <div class="join-button">Join now &gt;&gt;</div>
    <div class="url-text">brightplatekitchen.com</div>
  </section>
  <div class="size-label" style="left:328px;top:828px;width:326px">125x125</div>

</body>
</html>
```